Startup company business card (Media & Advertising)

we need a business card design for a company that is a startup in the media and aggregation industry. Card needs to look funky and of a new breed/modern and upmarket.

Target Market(s)

advertisers/ brand agencies & media publishers

Industry/Entity Type

Advertising

Contact Information for Business Card

Please ensure the front face signifies our brand (plumvexo.com) and back has details for the contact. Standard contact such as phone , address, email , website etc.

Font styles to use
Other font styles liked:
• use styleguide and logo font and color

Colors

Designer to choose colors to be used in the design.

Requirements
Must have
• We are disrupting the media and agency industry so subtlety would be good to use imagery to signify this
Nice to have
• Please use logo colors for branding
Should not have
• be as creative and provide few options. Pick a brand color from logo and styleguide

```html
<!DOCTYPE html>
<html lang="en">
<head>
<meta charset="utf-8">
<title>plumvexo business card</title>
<link rel="stylesheet" href="https://fonts.googleapis.com/css2?family=Roboto:wght@400;500;700&display=swap">
<style>
  :root {
    --backdrop: #2b2b2b;
    --card: #0c0c0d;
    --card-sheen: #1a1a1c;
    --brand-red: #e9435a;
    --text-light: #f2f2f2;
    --text-soft: #cfcfcf;
  }
  * { box-sizing: border-box; margin: 0; padding: 0; }
  html, body {
    width: 1200px; height: 896px; overflow: hidden;
    background: var(--backdrop);
    font-family: "Roboto", Arial, sans-serif;
  }
  .stage {
    width: 1200px; height: 896px;
    display: flex; align-items: center; justify-content: center; gap: 60px;
  }
  .card {
    position: relative;
    width: 520px; height: 300px;
    border-radius: 22px;
    background: linear-gradient(135deg, var(--card-sheen) 0%, var(--card) 55%);
    box-shadow: 0 18px 40px rgba(0,0,0,.45);
    overflow: hidden;
  }
  .brand { display: flex; align-items: center; gap: 14px; }
  .brand-dot { width: 34px; height: 34px; border-radius: 50%; background: var(--brand-red); }
  .brand-name { color: var(--text-light); font-weight: 700; font-size: 46px; letter-spacing: .5px; }

  .card-front { display: flex; align-items: center; justify-content: center; }

  .card-back .brand { position: absolute; left: 40px; top: 36px; gap: 10px; }
  .card-back .brand-dot { width: 24px; height: 24px; }
  .card-back .brand-name { font-size: 30px; }

  .divider {
    position: absolute; left: 40px; right: 40px; top: 172px;
    height: 1.5px; background: var(--brand-red);
  }
  .person { position: absolute; left: 40px; top: 124px; }
  .person-name { color: var(--brand-red); font-size: 20px; font-weight: 500; letter-spacing: .5px; text-transform: uppercase; }
  .person-role { color: var(--text-soft); font-size: 14px; margin-top: 2px; }

  .contacts { position: absolute; left: 40px; top: 190px; list-style: none; }
  .contacts li {
    display: flex; align-items: center; gap: 10px;
    color: var(--text-light); font-size: 15px; line-height: 26px; letter-spacing: .3px;
  }
  .contacts svg { width: 12px; height: 12px; flex: none; }

  .address {
    position: absolute; right: 40px; top: 190px;
    text-align: right; color: var(--text-light);
    font-size: 14px; line-height: 22px; font-style: normal;
  }
</style>
</head>
<body>
<main class="stage">
  <section class="card card-front" aria-label="Card front">
    <div class="brand">
      <span class="brand-dot"></span>
      <span class="brand-name">plumvexo</span>
    </div>
  </section>

  <section class="card card-back" aria-label="Card back">
    <div class="brand">
      <span class="brand-dot"></span>
      <span class="brand-name">plumvexo</span>
    </div>

    <div class="person">
      <p class="person-name">Daniel Warde</p>
      <p class="person-role">Director</p>
    </div>

    <div class="divider"></div>

    <ul class="contacts">
      <li>
        <svg viewBox="0 0 12 12" aria-hidden="true"><path d="M2.5 1h2l1 2.8-1.3.9a6 6 0 0 0 3.1 3.1l.9-1.3L11 7.5v2A1.5 1.5 0 0 1 9.5 11 8.5 8.5 0 0 1 1 2.5 1.5 1.5 0 0 1 2.5 1z" fill="var(--brand-red)"/></svg>
        +41795550148
      </li>
      <li>
        <svg viewBox="0 0 12 12" aria-hidden="true"><rect x="1" y="2.5" width="10" height="7" rx="1" fill="none" stroke="var(--brand-red)" stroke-width="1.2"/><path d="M1.5 3l4.5 3.5L10.5 3" fill="none" stroke="var(--brand-red)" stroke-width="1.2"/></svg>
        info@plumvexo.com
      </li>
      <li>
        <svg viewBox="0 0 12 12" aria-hidden="true"><circle cx="6" cy="6" r="5" fill="none" stroke="var(--brand-red)" stroke-width="1.2"/><path d="M1 6h10M6 1c-2.2 2.6-2.2 7.4 0 10M6 1c2.2 2.6 2.2 7.4 0 10" fill="none" stroke="var(--brand-red)" stroke-width="1"/></svg>
        www.plumvexo.com
      </li>
    </ul>

    <address class="address">
      27 Harbor Lane<br>
      Kelton, WA 98010
    </address>
  </section>
</main>
</body>
</html>
```